We need a business card design for a Dubai based company .

We need a business card for a Dubai based company called "Zernova Smoking Requisites Trading LLC". We mainly import Flavoured Tobacco products and Charcoal which is used for smoking in a Hookah/Shisha and distribute to the wholesalers and retailers. Logo file is attached herewith.

```html
<!DOCTYPE html>
<html lang="en">
<head>
<meta charset="utf-8">
<title>Zernova Smoking Requisites Trading LLC – Business Card</title>
<link rel="stylesheet" href="https://fonts.googleapis.com/css2?family=Jost:wght@400;500&family=Roboto:wght@400;700&display=swap">
<style>
  :root {
    --page-bg: #9b9b9b;
    --card-white: #ffffff;
    --brand-red: #b72a2f;
    --ink-black: #111111;
    --back-dark: #2a2a2a;
    --back-mark: #707070;
    --text-light: #ffffff;
  }
  html, body {
    margin: 0;
    padding: 0;
    overflow: hidden;
  }
  body {
    width: 1133px;
    height: 1200px;
    background: var(--page-bg);
    position: relative;
    font-family: "Jost", sans-serif;
  }
  .card {
    position: absolute;
    left: 200px;
    width: 722px;
    height: 414px;
    overflow: hidden;
  }
  .card--front { top: 144px; background: var(--card-white); }
  .card--back { top: 640px; background: var(--back-dark); }

  .front-panel {
    position: absolute;
    inset: 0;
  }

  .brand-block {
    position: absolute;
    left: 0;
    top: 0;
    width: 360px;
    height: 414px;
    display: flex;
    align-items: center;
    justify-content: center;
    gap: 12px;
  }
  .brand-square {
    width: 14px;
    height: 14px;
    background: var(--brand-red);
    flex: none;
  }
  .brand-name {
    color: var(--ink-black);
    font-weight: 500;
    line-height: 1;
    text-align: center;
  }
  .brand-name__main {
    display: block;
    font-size: 42px;
    letter-spacing: 4px;
  }
  .brand-name__sub {
    display: block;
    font-size: 8.5px;
    letter-spacing: 2.2px;
    margin-top: 8px;
  }

  .contact {
    position: absolute;
    left: 412px;
    top: 100px;
    color: var(--text-light);
  }
  .contact__name {
    font-family: "Roboto", sans-serif;
    font-weight: 700;
    font-size: 22px;
    margin: 0;
    line-height: 1;
    letter-spacing: 0.2px;
  }
  .contact__role {
    font-family: "Roboto", sans-serif;
    font-size: 17px;
    margin: 4px 0 0;
    line-height: 1.1;
  }
  .contact__address {
    font-style: normal;
    font-size: 17px;
    line-height: 20px;
    margin: 16px 0 0 3px;
  }
  .contact__list {
    list-style: none;
    margin: 11px 0 0 3px;
    padding: 0;
    font-size: 17px;
    line-height: 20.5px;
  }
  .contact__list li {
    display: flex;
    align-items: center;
    gap: 9px;
  }
  .contact__icon {
    width: 13px;
    height: 13px;
    flex: none;
    fill: var(--text-light);
  }

  .back-brand {
    position: absolute;
    inset: 0;
    display: flex;
    align-items: center;
    justify-content: center;
    gap: 14px;
  }
  .back-brand .brand-square { background: var(--back-mark); }
  .back-brand .brand-name { color: var(--back-mark); }
  .back-brand .brand-name__main { font-size: 50px; letter-spacing: 5px; }
  .back-brand .brand-name__sub { font-size: 10px; letter-spacing: 2.6px; }
</style>
</head>
<body>

<section class="card card--front" aria-label="Business card front">
  <svg class="front-panel" width="722" height="414" viewBox="0 0 722 414" aria-hidden="true">
    <polygon points="356,0 722,0 722,414 356,414 356,138 386,106 356,74" fill="var(--ink-black)"/>
    <polygon points="364,0 722,0 722,414 364,414 364,141 394,106 364,71" fill="var(--brand-red)"/>
  </svg>

  <div class="brand-block">
    <span class="brand-square"></span>
    <div class="brand-name">
      <span class="brand-name__main">ZERNOVA</span>
      <span class="brand-name__sub">SMOKING REQUISITES TRADING LLC</span>
    </div>
  </div>

  <div class="contact">
    <h1 class="contact__name">DANIEL HARTLEY</h1>
    <p class="contact__role">President</p>
    <address class="contact__address">4120 Harbor View Road<br>Juneau, Alaska 34518</address>
    <ul class="contact__list">
      <li>
        <svg class="contact__icon" viewBox="0 0 16 16"><path d="M3.5 1l2.5 3-1.5 2c1 2 3 4 5 5l2-1.5 3 2.5-1.5 2.5C8 15 1 8 1 2.5z"/></svg>
        369-408-1172
      </li>
      <li>
        <svg class="contact__icon" viewBox="0 0 16 16"><path d="M4 0h8v16H4zM5.5 2v10h5V2zM7 13.2h2v1.3H7z" fill-rule="evenodd"/></svg>
        369-730-2264
      </li>
      <li>
        <svg class="contact__icon" viewBox="0 0 16 16"><path d="M4 1h7v5H4zM1 7h14v6H1zM3 14h10v1.5H3z"/></svg>
        369-611-4093
      </li>
      <li>
        <svg class="contact__icon" viewBox="0 0 16 16"><path d="M1 3.5h14v9H1zM1.8 4.3L8 9l6.2-4.7" fill-rule="evenodd"/><path d="M1.5 4l6.5 5 6.5-5" stroke="var(--brand-red)" stroke-width="1.2" fill="none"/></svg>
        info@zernovasmokingrequisites.com
      </li>
      <li>
        <svg class="contact__icon" viewBox="0 0 16 16"><circle cx="8" cy="8" r="7"/><path d="M4 5c2 0 3 1 2 3s1 3 0 5M10 2.5c-1 2 1 3 3 3" stroke="var(--brand-red)" stroke-width="1.4" fill="none"/></svg>
        zernovasmokingrequisites.com
      </li>
    </ul>
  </div>
</section>

<section class="card card--back" aria-label="Business card back">
  <div class="back-brand">
    <span class="brand-square"></span>
    <div class="brand-name">
      <span class="brand-name__main">ZERNOVA</span>
      <span class="brand-name__sub">SMOKING REQUISITES TRADING LLC</span>
    </div>
  </div>
</section>

</body>
</html>
```